Keyvane - Premium Club Brochure

Up until now, we've used Canva to create the Brochure we have at-hand, the one attached to this enquiry.

I have been referred to ArtMuster by my Business Partner, Desmond Oakhurst.

We have recently established a New Real Estate Agency.

This Brochure is our Property Management Membership Brochure, describing the 3x Memberships (Gold, Platinum & Diamond) & outlining the Benefits & Bonuses that are included in these Memberships.

For ALL Pages, we are open to suggestions & other designs/templates/colour schemes.

Target Market(s)

Real Estate - Landlords / Investors

Industry/Entity Type

Real Estate

Font styles to use
Serif
Sans Serif

Colors

Designer to choose colors to be used in the design.

Requirements
Must have
• We would like to do the following:
• - Page 1:
• 1. Include under Email: info@keyvane.com.au
• 2. Include Website under Email (www.keyvane.com.au).
• Website
• www.keyvane.com.au
• 3. The Picture on the right, could we change that Photo to a Block of Apartments & remove the Lines going across the Picture.
• - Page 2
• 1. Create a Border around the Page.
• 2. Heading - Make it stand out more.
• 3. Create Banners for 'Quality Service' & '2.5% Lowest Fees'.
• 4. Categorise the Memberships with these Boarders, please refer to the attachment for example.
• 5. Annual Savings - Make it stand out more.
• - Page 3
• - Page 4
• Please for ALL Fonts, make them the same, we do NOT have the correct font programs to unify them.
Nice to have
• - Page 1:
• Website
• www.keyvane.com.au
• - Page 2:
• When it mentions "2.5% Lowest Fees', please feel free to provide any suggestions, we are open to any suggestions/ideas for this.
Should not have
• Grammar or Spelling errors.

```html
<!DOCTYPE html>
<html lang="en">
<head>
<meta charset="UTF-8">
<title>Keyvane – Brochure Cover Spread</title>
<link href="https://fonts.googleapis.com/css2?family=Montserrat:wght@400;600;700&family=Nunito+Sans:wght@400;600&display=swap" rel="stylesheet">
<style>
  :root {
    --page-bg: #1e1e1e;
    --ink: #06060b;
    --panel: #0b0b12;
    --yellow: #e2e02a;
    --grey: #4a4a4e;
    --rule: #2c2c33;
    --white: #ffffff;
    --muted: #d9d9de;
  }
  html, body {
    margin: 0;
    padding: 0;
    width: 893px;
    height: 1200px;
    overflow: hidden;
    background: var(--page-bg);
  }
  .canvas {
    position: relative;
    width: 893px;
    height: 1200px;
  }
  .spread-frame {
    position: absolute;
    left: 20px;
    top: 299px;
    width: 853px;
    height: 602px;
    overflow: hidden;
    box-shadow: 0 10px 30px rgba(0,0,0,.5);
  }
  .spread {
    position: relative;
    width: 942px;
    height: 665px;
    transform: scale(0.9055);
    transform-origin: 0 0;
    background: var(--ink);
    font-family: "Nunito Sans", Arial, sans-serif;
    color: var(--white);
  }
  .spread-art {
    position: absolute;
    inset: 0;
    width: 942px;
    height: 665px;
  }
  .brand {
    position: absolute;
    top: 376px;
    font-family: "Montserrat", Arial, sans-serif;
    font-weight: 400;
    font-size: 19px;
    letter-spacing: 9px;
    color: var(--white);
  }
  .brand--back { left: 167px; }
  .brand--front { left: 484px; }

  .back-cover {
    position: absolute;
    left: 0;
    top: 495px;
    width: 470px;
    text-align: center;
  }
  .offer {
    margin: 0;
    font-family: "Montserrat", Arial, sans-serif;
    font-weight: 600;
    font-size: 15px;
    line-height: 17px;
    text-transform: uppercase;
  }
  .offer__accent { color: var(--yellow); display: block; }
  .contact-title {
    margin: 52px 0 0;
    font-family: "Montserrat", Arial, sans-serif;
    font-weight: 700;
    font-size: 21px;
    color: var(--yellow);
  }
  .contact-list {
    position: absolute;
    top: 617px;
    left: 30px;
    display: flex;
    gap: 0;
    font-size: 11px;
    line-height: 14px;
    color: var(--white);
  }
  .contact-item {
    display: flex;
    align-items: flex-start;
    gap: 6px;
  }
  .contact-item--address { width: 150px; }
  .contact-item--hours { width: 132px; }
  .contact-item svg { flex: none; margin-top: 2px; }

  .front-cover {
    position: absolute;
    left: 490px;
    top: 500px;
    width: 430px;
    text-align: center;
  }
  .tagline {
    margin: 0;
    font-size: 10.5px;
    letter-spacing: .2px;
    text-transform: uppercase;
    color: var(--muted);
  }
  .headline {
    margin: 6px 0 0;
    font-family: "Montserrat", Arial, sans-serif;
    font-weight: 700;
    font-size: 40px;
    line-height: 37px;
    color: var(--yellow);
    text-transform: uppercase;
  }
  .intro {
    margin: 6px 0 0;
    font-size: 10.5px;
    line-height: 14px;
    text-transform: uppercase;
    color: var(--white);
  }
  .front-links {
    position: absolute;
    top: 638px;
    left: 590px;
    display: flex;
    align-items: center;
    font-size: 11px;
    color: var(--white);
  }
  .front-links__divider {
    width: 1px;
    height: 20px;
    background: var(--muted);
    margin: 0 8px;
  }
</style>
</head>
<body>
<div class="canvas">
  <div class="spread-frame">
    <div class="spread">
      <svg class="spread-art" viewBox="0 0 942 665" xmlns="http://www.w3.org/2000/svg">
        <defs>
          <linearGradient id="hero-tones" x1="0" y1="0" x2="0" y2="1">
            <stop offset="0" stop-color="#3f86d6"/>
            <stop offset="0.2" stop-color="#8fb8e6"/>
            <stop offset="0.3" stop-color="#c9ccd6"/>
            <stop offset="0.62" stop-color="#9aa3b4"/>
            <stop offset="0.74" stop-color="#4f8a2c"/>
            <stop offset="1" stop-color="#6aa53a"/>
          </linearGradient>
          <linearGradient id="thumb-interior" x1="0" y1="0" x2="1" y2="1">
            <stop offset="0" stop-color="#f2f2f0"/>
            <stop offset="1" stop-color="#b9bcbf"/>
          </linearGradient>
          <linearGradient id="thumb-skyline" x1="0" y1="0" x2="0" y2="1">
            <stop offset="0" stop-color="#8aa9cf"/>
            <stop offset="0.6" stop-color="#b58a5c"/>
            <stop offset="1" stop-color="#4c6d86"/>
          </linearGradient>
          <linearGradient id="thumb-harbour" x1="0" y1="0" x2="0" y2="1">
            <stop offset="0" stop-color="#6fa1d8"/>
            <stop offset="0.6" stop-color="#9aa6b4"/>
            <stop offset="1" stop-color="#2d5b86"/>
          </linearGradient>
        </defs>

        <rect class="hero-photo" x="0" y="0" width="942" height="400" fill="url(#hero-tones)" role="img" aria-label="Photo of a four-storey apartment block behind trees and a green lawn under blue sky"/>

        <polygon class="brand-band" points="0,348 692,348 652,420 0,420" fill="var(--panel)"/>
        <rect class="lower-panel" x="0" y="418" width="942" height="247" fill="var(--ink)"/>
        <polygon class="thumb-backing" points="600,395 942,395 942,480 580,480" fill="var(--ink)"/>

        <line x1="145" y1="348" x2="145" y2="418" stroke="var(--rule)" stroke-width="1.5"/>
        <line x1="462" y1="348" x2="462" y2="418" stroke="var(--rule)" stroke-width="1.5"/>

        <polygon class="accent-stripe" points="0,418 302,418 290,443 0,443" fill="var(--yellow)"/>
        <polygon class="grey-stripe" points="302,428 616,428 610,438 298,438" fill="var(--grey)"/>

        <polygon points="610,397 712,397 690,470 592,470" fill="url(#thumb-interior)" role="img" aria-label="Photo of a bright empty apartment interior"/>
        <polygon points="726,397 840,397 818,470 704,470" fill="url(#thumb-skyline)" role="img" aria-label="Photo of a city skyline across the water"/>
        <polygon points="852,397 942,397 942,470 830,470" fill="url(#thumb-harbour)" role="img" aria-label="Photo of a harbour city skyline"/>
        <polygon class="thumb-underline" points="592,472 942,472 942,481 584,481" fill="var(--yellow)"/>

        <rect x="822" y="643" width="120" height="4" fill="var(--yellow)"/>
      </svg>

      <div class="brand brand--back">KEYVANE</div>
      <div class="brand brand--front">KEYVANE</div>

      <section class="back-cover">
        <p class="offer">Lease your property in the next 14 days or
          <span class="offer__accent">we'll cover your rent!</span></p>
        <h2 class="contact-title">CONTACT US TODAY</h2>
      </section>

      <div class="contact-list">
        <div class="contact-item contact-item--address">
          <svg width="8" height="10" viewBox="0 0 8 10"><path d="M4 0a3.5 3.5 0 0 0-3.5 3.5C.5 6 4 10 4 10s3.5-4 3.5-6.5A3.5 3.5 0 0 0 4 0zm0 5a1.4 1.4 0 1 1 0-2.8A1.4 1.4 0 0 1 4 5z" fill="var(--yellow)"/></svg>
          <span>42 Harbourview Lane<br>Sydney, Australia</span>
        </div>
        <div class="contact-item contact-item--hours">
          <svg width="11" height="10" viewBox="0 0 11 10"><rect x=".5" y="1.5" width="10" height="8" rx="1" fill="none" stroke="var(--yellow)"/><rect x=".5" y="1.5" width="10" height="2.5" fill="var(--yellow)"/><rect x="2.5" y="5.5" width="1.5" height="1.5" fill="var(--yellow)"/><rect x="5" y="5.5" width="1.5" height="1.5" fill="var(--yellow)"/><rect x="7.5" y="5.5" width="1.5" height="1.5" fill="var(--yellow)"/></svg>
          <span>9AM – 5PM<br>Monday – Friday</span>
        </div>
        <div class="contact-item">
          <svg width="10" height="26" viewBox="0 0 10 26"><path d="M1 2.5h8v2H7.5L6.5 3.5h-3l-1 1H1z" fill="var(--yellow)"/><rect x="2" y="5" width="6" height="4" rx="1" fill="var(--yellow)"/><circle cx="5" cy="19" r="4" fill="none" stroke="var(--yellow)" stroke-width="1.2"/><path d="M1 19h8M5 15c-2 2.5-2 5.5 0 8M5 15c2 2.5 2 5.5 0 8" fill="none" stroke="var(--yellow)" stroke-width=".8"/></svg>
          <span>02 5550 1428<br>www.keyvane.com.au</span>
        </div>
      </div>

      <section class="front-cover">
        <p class="tagline">Residential, commercial &amp; investment property agents Sydney</p>
        <h1 class="headline">Real estate for<br>your world</h1>
        <p class="intro">We have matched our real estate experiences with the cutting<br>edge information technological advances.</p>
      </section>

      <div class="front-links">
        <span>info@keyvane.com.au</span>
        <span class="front-links__divider"></span>
        <span>www.keyvane.com.au</span>
      </div>
    </div>
  </div>
</div>
</body>
</html>
```